Artificial Intelligence based service LanePilot.ai

Looking for a website for service designed for driving schools to deliver AI based solutions and features. File are to include various pages from contact to list of services to faqs, demos and more. we are looking for a website for AI based service for driving schools. services will include things like chat bots, voice agent, document processing and ai based marketing.

Target Market(s)

driving school owners and managers.

Industry/Entity Type

software and AI

Number of Pages Required

4 page

Font styles to use
Sans Serif

Requirements
Must have
• clean and easy to navigate pages. responsive. also delivery via FIGMA.

```html
<!DOCTYPE html>
<html lang="en">
<head>
<meta charset="UTF-8">
<title>LanePilot.ai — 24/7 Voice Agent for Driving Schools</title>
<link href="https://fonts.googleapis.com/css2?family=Michroma&family=Poppins:wght@400;500;600&display=swap" rel="stylesheet">
<style>
:root{
  --navy:#0b1f4d;
  --navy-deep:#07163a;
  --green:#6fb56b;
  --ink:#1c2233;
  --muted:#5a6072;
  --panel:#f0f1f5;
  --white:#ffffff;
}
*{box-sizing:border-box;margin:0;padding:0}
html,body{width:1200px;height:3836px;overflow:hidden;background:var(--white)}
body{position:relative;font-family:'Poppins',sans-serif;color:var(--ink)}
.abs{position:absolute}
.display{font-family:'Michroma',sans-serif;color:var(--navy);font-weight:400}
.accent{color:var(--green)}
.btn{position:absolute;display:flex;align-items:center;justify-content:center;font-size:9px;font-weight:600;text-transform:uppercase;letter-spacing:.2px;border-radius:3px}
.btn-navy{background:var(--navy);color:var(--white)}
.btn-green{background:var(--green);color:var(--white)}
.btn-outline{border:1.5px solid var(--navy);color:var(--navy);background:var(--white)}
.btn-white{background:var(--white);color:var(--navy)}
.btn-ghost{border:1.5px solid var(--white);color:var(--white)}

/* header */
.brand{position:absolute;font-family:'Poppins',sans-serif;font-weight:600;color:var(--navy);font-size:30px;letter-spacing:-.3px}
.nav{position:absolute;top:36px;left:410px;display:flex;align-items:center;gap:0;font-size:12px;color:var(--ink)}
.nav a{position:absolute;white-space:nowrap;color:var(--ink);text-decoration:none}

/* hero */
.hero-title{left:94px;top:176px;font-size:35px;line-height:38px;width:480px}
.hero-sub{left:94px;top:306px;font-size:12px;color:var(--muted)}
.photo{position:absolute;border-radius:28px}
.photo-students{left:622px;top:107px;width:541px;height:620px;background:linear-gradient(135deg,#6fc24f,#3d6a2e 55%,#a58a6e)}
.photo-office{left:33px;top:487px;width:512px;height:240px;background:linear-gradient(120deg,#5b4a3c,#c9cfd6 45%,#6b7c5a)}

/* why band */
.why-band{left:33px;top:789px;width:1123px;height:566px;border-radius:26px;background:radial-gradient(ellipse at 10% 85%,#1d4a8a 0%,transparent 35%),radial-gradient(ellipse at 92% 75%,#1d4a8a 0%,transparent 30%),var(--navy)}
.why-title{left:0;width:1200px;top:880px;text-align:center;color:var(--white);font-size:34px;line-height:38px}
.why-text{left:270px;width:660px;top:972px;text-align:center;color:#e6e9f2;font-size:12px;line-height:20px}
.photo-team{left:249px;top:1065px;width:702px;height:397px;border-radius:22px;background:linear-gradient(120deg,#dcd6d2,#6c6a6a 45%,#24424a 80%,#9fb8c0)}

/* problems */
.section-title{left:0;width:1200px;text-align:center;font-size:34px}
.problem{position:absolute;left:200px;width:802px;background:var(--panel);border-radius:16px}
.problem.active{background:var(--white);border:1.5px solid #b9d8b6}
.problem .icon{position:absolute;left:28px;width:46px;height:46px;border-radius:50%;background:var(--navy);display:flex;align-items:center;justify-content:center}
.problem.active .icon{background:var(--green)}
.problem h3{position:absolute;left:92px;font-family:'Michroma',sans-serif;font-weight:400;font-size:17px;color:var(--navy)}
.problem p{position:absolute;left:92px;font-size:11.5px;color:var(--muted);line-height:19px}
.problem p b{color:var(--ink);font-weight:600}
.problem .arrow{position:absolute;right:36px;width:30px;height:30px;border-radius:50%;background:var(--white);display:flex;align-items:center;justify-content:center}
.problem.active .arrow{background:var(--green)}

/* benefits */
.benefits-bg{left:0;top:2228px;width:1200px;height:520px;background:var(--panel);border-radius:36px}
.benefit{position:absolute;width:262px;height:112px;background:var(--white);border-radius:12px;font-family:'Michroma',sans-serif;font-size:12px;line-height:16px;color:var(--navy);padding:52px 0 0 45px;box-shadow:0 2px 6px rgba(0,0,0,.03)}
.benefit-icon{left:506px;top:2379px;width:54px;height:54px;border-radius:50%;background:var(--green);border:3px solid var(--white);display:flex;align-items:center;justify-content:center}

/* cta */
.cta{left:0;top:2737px;width:1200px;height:509px;border-radius:24px;background:linear-gradient(100deg,#0d2a66 0%,#123a7a 35%,#1b3a6a 60%,#2d2a24 100%)}
.cta-title{left:0;width:1200px;top:2925px;text-align:center;color:var(--white);font-size:32px;line-height:40px}
.cta-sub{left:0;width:1200px;top:3001px;text-align:center;color:#e6e9f2;font-size:12px}

/* testimonial */
.quote{left:0;width:1200px;text-align:center}
.quote-text{top:3410px;font-size:23px;line-height:34px;color:#4a4f5e}
.quote-name{top:3488px;font-family:'Michroma',sans-serif;font-size:12px;color:var(--navy)}
.quote-org{top:3509px;font-size:11px;color:var(--muted)}

/* footer */
.footer{left:0;top:3615px;width:1200px;height:221px;background:var(--panel);border-radius:36px 36px 0 0}
.copyright{left:0;width:1200px;top:3757px;text-align:center;font-size:11px;color:var(--muted)}
.to-top{left:1122px;top:3728px;width:34px;height:34px;border-radius:50%;background:var(--green);display:flex;align-items:center;justify-content:center}
</style>
</head>
<body>

<!-- header -->
<div class="brand" style="left:92px;top:34px">LanePilot.ai</div>
<svg class="abs" style="left:409px;top:40px" width="14" height="12" viewBox="0 0 14 12"><path d="M7 0 14 6h-2v6H9V8H5v4H2V6H0z" fill="#6fb56b"/></svg>
<nav>
  <a class="abs" style="left:445px;top:38px;font-size:12px;color:#1c2233">Services</a>
  <a class="abs" style="left:534px;top:38px;font-size:12px;color:#1c2233">Demo / See It in Action</a>
  <a class="abs" style="left:702px;top:38px;font-size:12px;color:#1c2233">Pricing</a>
  <a class="abs" style="left:774px;top:38px;font-size:12px;color:#1c2233">FAQs</a>
  <a class="abs" style="left:836px;top:38px;font-size:12px;color:#1c2233">About Us</a>
  <a class="abs" style="left:921px;top:38px;font-size:12px;color:#1c2233">Contact</a>
</nav>
<div class="btn btn-outline" style="left:993px;top:31px;width:113px;height:32px">Book a Free Demo</div>

<!-- hero -->
<h1 class="abs display hero-title">Boost Your Driving School with a <span class="accent">24/7</span> Voice Agent</h1>
<p class="abs hero-sub">Automate Calls. Answer Questions Instantly. Never Miss a Student Again.</p>
<div class="btn btn-navy" style="left:94px;top:336px;width:109px;height:29px">See It in Action</div>
<div class="photo photo-students" role="img" aria-label="Smiling student driver in a green car with instructor giving a thumbs up"></div>
<div class="photo photo-office" role="img" aria-label="Robot assistant working at a desk beside call center staff"></div>
<div class="btn btn-green" style="left:186px;top:465px;width:180px;height:26px;border-radius:4px 4px 0 0">Talk to a Product Specialist</div>

<!-- why -->
<div class="abs why-band"></div>
<h2 class="abs display why-title">Why Driving Schools Choose<br><span class="accent">Voice</span> Agents</h2>
<p class="abs why-text">Running a driving school means juggling lesson schedules, student questions, staff changes, and constant phone calls. A Voice Agent is your AI-powered assistant that answers the phone 24/7, handles routine questions, and gives your staff room to breathe—without the cost of hiring more people.</p>
<div class="abs photo-team" role="img" aria-label="Two colleagues reviewing data on computer monitors in an office"></div>

<!-- problems -->
<h2 class="abs display section-title" style="top:1566px">Key Problems Solved</h2>

<div class="problem" style="top:1633px;height:102px">
  <div class="icon" style="top:28px"><svg width="18" height="18" viewBox="0 0 24 24"><path d="M6.6 10.8a15 15 0 0 0 6.6 6.6l2.2-2.2c.3-.3.7-.4 1-.2 1.1.4 2.3.6 3.6.6.6 0 1 .4 1 1V20c0 .6-.4 1-1 1A17 17 0 0 1 3 4c0-.6.4-1 1-1h3.5c.6 0 1 .4 1 1 0 1.3.2 2.5.6 3.6.1.3 0 .7-.2 1z" fill="#fff"/></svg></div>
  <h3 style="top:30px">High Call Volume &amp; Repetitive Questions</h3>
  <p style="top:54px">Let your voice agent handle calls about:</p>
  <div class="arrow" style="top:36px"><svg width="12" height="12" viewBox="0 0 12 12"><path d="M2 10 10 2M4 2h6v6" stroke="#0b1f4d" stroke-width="1.3" fill="none"/></svg></div>
</div>

<div class="problem active" style="top:1744px;height:117px">
  <div class="icon" style="top:34px"><svg width="18" height="18" viewBox="0 0 24 24"><circle cx="12" cy="12" r="9" fill="#fff"/><path d="M12 7v5l3 2" stroke="#6fb56b" stroke-width="2" fill="none"/></svg></div>
  <h3 style="top:26px">After-Hours Availability</h3>
  <p style="top:51px">Missed calls = missed business. Your voice agent works evenings, weekends, and holidays.<br><b>Result:</b> Convert more inquiries into paying students—even while you sleep.</p>
  <div class="arrow" style="top:42px"><svg width="12" height="12" viewBox="0 0 12 12"><path d="M2 2 10 10M10 4v6H4" stroke="#fff" stroke-width="1.3" fill="none"/></svg></div>
</div>

<div class="problem" style="top:1873px;height:100px">
  <div class="icon" style="top:27px"><svg width="18" height="18" viewBox="0 0 24 24"><circle cx="12" cy="8" r="4" fill="#fff"/><path d="M4 21c0-4.4 3.6-7 8-7s8 2.6 8 7z" fill="#fff"/></svg></div>
  <h3 style="top:28px">Admin Staff Turnover</h3>
  <p style="top:53px">Hiring and training office staff takes time. A voice agent is ready on day one.</p>
  <div class="arrow" style="top:35px"><svg width="12" height="12" viewBox="0 0 12 12"><path d="M2 10 10 2M4 2h6v6" stroke="#0b1f4d" stroke-width="1.3" fill="none"/></svg></div>
</div>

<div class="problem" style="top:1983px;height:100px">
  <div class="icon" style="top:27px"><svg width="18" height="18" viewBox="0 0 24 24"><circle cx="12" cy="8" r="4" fill="#fff"/><path d="M4 21c0-4.4 3.6-7 8-7s8 2.6 8 7z" fill="#fff"/></svg></div>
  <h3 style="top:28px">Instructor Absences &amp; Rescheduling</h3>
  <p style="top:53px">Integrated with your booking system, your voice agent can help reschedule or notify students of changes.</p>
  <div class="arrow" style="top:35px"><svg width="12" height="12" viewBox="0 0 12 12"><path d="M2 10 10 2M4 2h6v6" stroke="#0b1f4d" stroke-width="1.3" fill="none"/></svg></div>
</div>

<div class="btn btn-navy" style="left:545px;top:2100px;width:110px;height:30px">Load More</div>

<!-- benefits -->
<div class="abs benefits-bg"></div>
<h2 class="abs display section-title" style="top:2320px">Real Benefits for Your School</h2>
<div class="benefit" style="left:200px;top:2408px">24/7 live call support—<br>no more missed calls</div>
<div class="benefit" style="left:469px;top:2408px">Faster response times<br>happier customers</div>
<div class="benefit" style="left:740px;top:2408px">Less admin stress for<br>you and your team</div>
<div class="benefit" style="left:200px;top:2531px">Lower operating costs<br>than live staff</div>
<div class="benefit" style="left:469px;top:2531px">More bookings,<br>fewer no-shows</div>
<div class="benefit" style="left:740px;top:2531px">A modern,<br>professional image</div>
<div class="abs benefit-icon"><svg width="22" height="24" viewBox="0 0 22 24"><rect x="3" y="2" width="16" height="20" rx="2" stroke="#fff" stroke-width="1.6" fill="none"/><path d="M7 7h8M7 11h8" stroke="#fff" stroke-width="1.4"/><circle cx="11" cy="16" r="2.5" stroke="#fff" stroke-width="1.4" fill="none"/></svg></div>

<!-- cta -->
<div class="abs cta" role="img" aria-label="Man typing at a computer in a dim office with a glowing digital wave backdrop"></div>
<h2 class="abs display cta-title">Ready to Automate<br>Your Front Desk?</h2>
<p class="abs cta-sub">Let your school sound smarter, faster, and more helpful—24 hours a day.</p>
<div class="btn btn-white" style="left:393px;top:3039px;width:109px;height:28px">See It in Action</div>
<div class="btn btn-green" style="left:508px;top:3039px;width:178px;height:28px">Talk to a Product Specialist</div>
<div class="btn btn-ghost" style="left:692px;top:3039px;width:115px;height:28px">Book a Free Demo</div>

<!-- testimonial -->
<svg class="abs" style="left:570px;top:3343px" width="60" height="46" viewBox="0 0 60 46"><path d="M0 46V26C0 10 8 2 24 0v9c-8 2-11 7-11 14h11v23zM34 46V26C34 10 42 2 58 0v9c-8 2-11 7-11 14h11v23z" fill="#6fb56b"/></svg>
<p class="abs quote quote-text">Since adding a voice agent, we’ve cut our call<br>volume in half—and enrollment is up!</p>
<p class="abs quote quote-name">Dana Whitfield, Director</p>
<p class="abs quote quote-org">GreenLight Driving Academy</p>

<!-- footer -->
<div class="abs footer"></div>
<div class="brand" style="left:0;width:1200px;text-align:center;top:3700px">LanePilot.ai</div>
<p class="abs copyright">©Copyright 2025 | All Rights Reserved</p>
<div class="abs to-top"><svg width="10" height="8" viewBox="0 0 10 8"><path d="M1 6 5 2l4 4" stroke="#fff" stroke-width="1.6" fill="none"/></svg></div>

</body>
</html>
```